Shopify design for a sensor shop

Addendum - I have added a Cart Page that seems to have been missed in the design received. This is an important aspect of the projects.
I am looking for a design for a website to suit the same branding as our homepage - www.lumetrix.io

The idea is the user can click on a project type such as a school -
https://www.lumetrix.io/pricing

And then add and edit device numbers almost like quince shop when configuring a laptop.

The 3 shops that are in this space, but too complicated are the following:
https://brightgadgetry.store/gb/
https://www.keenhousinggoods.co.uk/products/
https://www.vortal47.co.uk/shop/

There can be 100's of devices all with different manufacturers and Models with different sensors - such as temperature, co2, Electrical Meters etc - so it needs a good filter.

Brand guideline:
https://www.pillargatehub.com/lumetrix/brand/overview

the winning design will have knowledge of what's possible using Shopify, now designs that cannot be built. If they can also build this will be a bonus, but not a requirement.

This will be an ongoing assignment - with additional pages to be added after the first design is used to build the MVP of the shop.

Target Market(s)

B2B IoT SaaS

Industry/Entity Type

IoT

Number of Pages Required

3 page

Requirements
Must have
• Similar design to existing website - Products Page, Cart, Products list.
Nice to have
• The page where devices can be added and edited is almost like the Quince store - https://www.quince.com/uk/shop/buy-tarn/tarn-forge/20-core-cpu-48-core-gpu-32-core-neural-engine-64gb-memory-1tb

```html
<!DOCTYPE html>
<html lang="en">
<head>
<meta charset="utf-8">
<title>Lumetrix Shop – Product</title>
<link rel="stylesheet" href="https://fonts.googleapis.com/css2?family=Jost:wght@400;500;600&family=Montserrat:wght@600;700&display=swap">
<style>
  :root{
    --ink:#0d1220;
    --text:#1e1e1e;
    --muted:#5b6572;
    --line:#2a2a2a;
    --page:#fafafa;
    --footer:#f5f5f5;
    --photo:#eeeeee;
    --photo-2:#e2e2e2;
    --star:#f59a23;
    --white:#ffffff;
  }
  *{box-sizing:border-box;margin:0;padding:0}
  html,body{width:1200px;height:2430px;overflow:hidden}
  body{position:relative;background:var(--page);font-family:'Jost',sans-serif;color:var(--text)}
  .abs{position:absolute}

  /* header */
  .site-header{left:0;top:0;width:1200px;height:62px;background:var(--page);box-shadow:0 1px 3px rgba(0,0,0,.05)}
  .brand{left:134px;top:14px;display:flex;align-items:center;gap:8px;font-family:'Jost',sans-serif;font-weight:500;font-size:24px;color:var(--ink);letter-spacing:-.3px}
  .brand-mark{width:22px;height:22px;background:var(--ink)}
  .nav-link{top:23px;font-size:13px;letter-spacing:.5px;color:var(--muted)}
  .nav-link.is-active{color:var(--ink);font-weight:500}
  .btn-solid,.btn-outline{display:flex;align-items:center;justify-content:center;font-size:13px;font-weight:500;letter-spacing:.3px}
  .btn-solid{background:var(--ink);color:var(--white)}
  .btn-outline{border:1.5px solid var(--ink);color:var(--ink);background:var(--white)}

  /* gallery */
  .photo{background:radial-gradient(circle at 50% 45%,#fbfbfb 0,var(--photo) 55%,var(--photo-2) 100%)}
  .gallery-main{left:130px;top:123px;width:443px;height:441px}
  .thumb{top:580px;width:140px;height:105px}
  .dots{left:329px;top:709px;display:flex;gap:5px}
  .dot{width:8px;height:8px;border-radius:50%;border:1.3px solid var(--ink)}
  .dot.is-current{width:6px;height:6px;margin:1px;border:none;background:var(--star)}

  /* buy panel */
  .rating{left:626px;top:118px;display:flex;align-items:center;gap:3px;font-size:10px}
  .rating span{margin-left:6px}
  .product-title{left:623px;top:145px;font-family:'Montserrat',sans-serif;font-weight:600;font-size:17px;color:var(--ink)}
  .product-lede{left:623px;top:179px;width:430px;font-size:12.5px;line-height:14.5px}
  .feature-list{left:625px;top:226px;list-style:none;font-size:12.5px;line-height:24.5px}
  .price{left:624px;top:312px;display:flex;align-items:center;gap:11px}
  .price-now{font-family:'Montserrat',sans-serif;font-weight:600;font-size:19px;color:var(--ink)}
  .price-was{font-size:12.5px;text-decoration:line-through}
  .price-tag{background:var(--ink);color:var(--white);font-size:10.5px;padding:3px 6px;border-radius:2px}
  .divider{left:625px;width:446px;height:1px;background:var(--line)}
  .option-label{left:624px;font-size:14px;font-weight:500;color:var(--ink)}
  .chip{display:flex;align-items:center;justify-content:center;border:1px solid var(--ink);border-radius:3px;font-size:11px;background:var(--white);color:var(--ink)}
  .chip.is-selected{background:var(--ink);color:var(--white);font-weight:500}
  .qty{left:628px;top:627px;width:222px;height:35px;border:1px solid var(--ink);border-radius:2px;background:var(--white);font-size:11px;padding:0 17px;display:flex;align-items:center;justify-content:space-between}
  .buy-now{left:630px;top:679px;width:141px;height:46px;font-size:15.5px;font-weight:600;border-radius:2px}

  /* box contents */
  .section-title{font-family:'Montserrat',sans-serif;font-weight:600;color:var(--ink)}
  .box-heading{left:0;width:1200px;top:805px;text-align:center;font-size:19.5px}
  .box-item{top:870px;width:448px;height:326px}
  .box-caption{top:1217px;width:448px;text-align:center;font-size:16.5px;color:#333}

  /* description */
  .desc-heading{left:131px;top:1305px;font-size:18.5px}
  .desc-body{left:132px;top:1347px;width:938px;font-size:12.3px;line-height:17.5px;text-align:justify}
  .desc-body p+p{margin-top:17.5px}

  /* related */
  .related-heading{left:131px;top:1702px;font-size:14px;font-family:'Montserrat',sans-serif;font-weight:700;letter-spacing:.2px;color:var(--ink)}
  .carousel-arrow{top:1708px}
  .card{top:1750px;width:210px;height:325px;border:1px solid #9a9a9a;background:var(--white)}
  .card-photo{position:absolute;left:45px;top:24px;width:120px;height:130px;background:radial-gradient(circle at 50% 45%,#f6f6f6,#e4e4e4 70%,#ffffff 100%)}
  .card-name{position:absolute;left:0;top:181px;width:100%;text-align:center;font-size:12px;line-height:16.5px}
  .card-price{position:absolute;left:0;top:234px;width:100%;text-align:center;font-size:12px}
  .card-price b{font-weight:600}
  .card-cart{position:absolute;left:62px;top:272px;width:85px;height:26px;border:1px solid var(--ink);display:flex;align-items:center;justify-content:center;font-size:10.5px}

  /* footer */
  .site-footer{left:0;top:2101px;width:1200px;height:329px;background:var(--footer)}
  .news-title{left:154px;top:2148px;font-size:16px;font-weight:500;color:#5a6270}
  .news-sub{left:154px;top:2170px;font-size:13px;color:#6e7684;letter-spacing:.2px}
  .news-input{left:610px;top:2145px;width:305px;height:44px;border:1px solid #c8c8c8;background:var(--white);font-size:13px;color:#8a919c;padding-left:13px;display:flex;align-items:center;letter-spacing:.2px}
  .news-submit{left:914px;top:2145px;width:152px;height:44px;font-size:13px}
  .footer-rule{left:154px;top:2219px;width:912px;height:1px;background:#e3e3e3}
  .footer-col{top:2245px;font-size:13px;color:#6e7684;letter-spacing:.2px}
  .footer-col h4{font-weight:500;font-size:16px;color:#6e7684;margin-bottom:5px}
  .footer-col li{list-style:none;line-height:20px}
  .copyright{left:0;top:2392px;width:1184px;text-align:center;font-size:11px;color:#6e7684}
</style>
</head>
<body>

<header class="site-header abs">
  <div class="brand abs"><span class="brand-mark"></span>Lumetrix</div>
  <a class="nav-link abs" style="left:312px">How it Works</a>
  <a class="nav-link abs is-active" style="left:434px">Outcomes</a>
  <a class="nav-link abs" style="left:535px">Pricing</a>
  <a class="btn-solid abs" style="left:838px;top:16px;width:125px;height:32px">Get In Touch</a>
  <a class="btn-outline abs" style="left:971px;top:14px;width:97px;height:36px">Sign In</a>
</header>

<main>
  <div class="gallery-main photo abs" role="img" aria-label="White square motion sensor with logo, front three-quarter view"></div>
  <div class="thumb photo abs" style="left:132px" role="img" aria-label="Sensor thumbnail, angled view"></div>
  <div class="thumb photo abs" style="left:286px" role="img" aria-label="Sensor thumbnail, front view"></div>
  <div class="thumb photo abs" style="left:437px" role="img" aria-label="Sensor thumbnail, side view"></div>
  <div class="dots abs"><i class="dot"></i><i class="dot is-current"></i><i class="dot"></i><i class="dot"></i><i class="dot"></i></div>

  <div class="rating abs">
    <svg width="76" height="13" viewBox="0 0 76 13" aria-hidden="true">
      <g fill="#f59a23">
        <path id="s" d="M6.5 0.5l1.8 3.8 4.1.5-3 2.9.8 4.1-3.7-2-3.7 2 .8-4.1-3-2.9 4.1-.5z"/>
        <use href="#s" x="15"/><use href="#s" x="30"/><use href="#s" x="45"/><use href="#s" x="60"/>
      </g>
    </svg>
    <span>4.8</span><span>(52 Reviews)</span>
  </div>
  <h1 class="product-title abs">Lorem Ipsum is simply dummy text of the printing</h1>
  <p class="product-lede abs">There are many variations of passages of Lorem Ipsum available, but the majority have suffered alteration in some form</p>
  <ul class="feature-list abs">
    <li>Lorem Ipsum is simply dummy text</li>
    <li>Contrary to popular belief, Lorem</li>
    <li>There are many variations of passages of Lorem</li>
  </ul>
  <div class="price abs"><span class="price-now">£279.00</span><span class="price-was">£1059.00</span><span class="price-tag">50% off</span></div>

  <div class="divider abs" style="top:362px"></div>
  <div class="option-label abs" style="top:375px">Category</div>
  <div class="chip is-selected abs" style="left:624px;top:407px;width:75px;height:35px">Battery</div>
  <div class="chip abs" style="left:707px;top:407px;width:80px;height:35px">Electrical</div>
  <div class="chip abs" style="left:795px;top:407px;width:95px;height:35px">Lorem IPsum</div>

  <div class="divider abs" style="top:467px"></div>
  <div class="option-label abs" style="top:487px">Size</div>
  <div class="chip abs" style="left:624px;top:520px;width:75px;height:35px">Pack 1</div>
  <div class="chip is-selected abs" style="left:707px;top:520px;width:80px;height:35px">Pack 2</div>
  <div class="chip abs" style="left:795px;top:520px;width:95px;height:35px">Pack 5</div>
  <div class="chip abs" style="left:898px;top:520px;width:95px;height:35px">Pack 8</div>

  <div class="divider abs" style="top:583px"></div>
  <div class="option-label abs" style="top:600px">Add Qty</div>
  <div class="qty abs"><span>1</span>
    <svg width="8" height="12" viewBox="0 0 8 12" aria-hidden="true"><path d="M4 0L8 5H0zM4 12L0 7h8z" fill="#0d1220"/></svg>
  </div>
  <a class="btn-solid buy-now abs">Buy Now</a>

  <h2 class="section-title box-heading abs">What’s in the Box</h2>
  <div class="box-item photo abs" style="left:131px" role="img" aria-label="Square white motion sensor"></div>
  <div class="box-item photo abs" style="left:622px" role="img" aria-label="Coiled black power cable with plug"></div>
  <div class="box-caption abs" style="left:131px">Sensor</div>
  <div class="box-caption abs" style="left:622px">Powercable</div>

  <h2 class="section-title desc-heading abs">Product Description</h2>
  <div class="desc-body abs">
    <p>Sed ut perspiciatis unde omnis iste natus error sit voluptatem accusantium doloremque laudantium, totam rem aperiam, eaque ipsa quae ab illo inventore veritatis et quasi architecto beatae vitae dicta sunt explicabo. Nemo enim ipsam voluptatem quia voluptas sit aspernatur aut odit aut fugit, sed quia consequuntur magni dolores eos qui ratione voluptatem sequi nesciunt. Neque porro quisquam est, qui dolorem ipsum quia dolor sit amet, consectetur, adipisci velit, sed quia non numquam eius modi tempora incidunt ut labore et dolore magnam aliquam quaerat voluptatem. Ut enim ad minima veniam, quis nostrum exercitationem ullam corporis suscipit laboriosam, nisi ut aliquid ex ea commodi consequatur? Quis autem vel eum iure reprehenderit qui in ea voluptate velit esse quam nihil molestiae consequatur, vel illum qui dolorem eum fugiat quo voluptas nulla pariatur</p>
    <p>But I must explain to you how all this mistaken idea of denouncing pleasure and praising pain was born and I will give you a complete account of the system, and expound the actual teachings of the great explorer of the truth, the master-builder of human happiness. No one rejects, dislikes, or avoids pleasure itself, because it is pleasure, but because those who do not know how to pursue pleasure rationally encounter consequences that are extremely painful. Nor again is there anyone who loves or pursues or desires to obtain pain of itself, because it is pain, but because occasionally circumstances occur in which toil and pain can procure him some great pleasure. To take a trivial example, which of us ever undertakes laborious physical exercise, except to obtain some advantage from it? But who has any right to find fault with a man who chooses to enjoy a pleasure that has no annoying consequences, or one who avoids a pain that produces no resultant pleasure?</p>
    <p>There are many variations of passages of Lorem Ipsum available, but the majority have suffered alteration in some form, by injected humour, or randomised words which don't look even slightly believable. If you are going to use a passage of Lorem Ipsum, you need to be sure there isn't anything embarrassing hidden in the middle of text. All the Lorem Ipsum generators on the Internet tend to repeat predefined chunks as necessary, making this the first true generator on the Internet.</p>
  </div>

  <h2 class="related-heading abs">OTHER PRODUCTS</h2>
  <svg class="carousel-arrow abs" style="left:1026px" width="16" height="20" viewBox="0 0 16 20" aria-label="Previous"><path d="M11 2L3 10l8 8" fill="none" stroke="#0d1220" stroke-width="2"/></svg>
  <svg class="carousel-arrow abs" style="left:1055px" width="16" height="20" viewBox="0 0 16 20" aria-label="Next"><path d="M5 2l8 8-8 8" fill="none" stroke="#0d1220" stroke-width="2"/></svg>

  <article class="card abs" style="left:130px">
    <div class="card-photo" role="img" aria-label="White wall-mounted PIR motion detector"></div>
    <p class="card-name">Lorem Ipsum is simply dum<br>text of the printing and</p>
    <p class="card-price"><b>£279.00</b> Excl. Tax</p>
    <a class="card-cart">Add to Cart</a>
  </article>
  <article class="card abs" style="left:371px">
    <div class="card-photo" role="img" aria-label="White siren unit with red strobe"></div>
    <p class="card-name">Lorem Ipsum is simply dum<br>text of the printing and</p>
    <p class="card-price"><b>£279.00</b> Excl. Tax</p>
    <a class="card-cart">Add to Cart</a>
  </article>
  <article class="card abs" style="left:614px">
    <div class="card-photo" role="img" aria-label="Round white ceiling smoke detector"></div>
    <p class="card-name">Lorem Ipsum is simply dum<br>text of the printing and</p>
    <p class="card-price"><b>£279.00</b> Excl. Tax</p>
    <a class="card-cart">Add to Cart</a>
  </article>
  <article class="card abs" style="left:858px;top:1752px">
    <div class="card-photo" role="img" aria-label="White outdoor motion sensor on bracket"></div>
    <p class="card-name">Lorem Ipsum is simply dum<br>text of the printing and</p>
    <p class="card-price"><b>£279.00</b> Excl. Tax</p>
    <a class="card-cart">Add to Cart</a>
  </article>
</main>

<footer class="site-footer abs"></footer>
<h3 class="news-title abs">Subscribe to our newsletter</h3>
<p class="news-sub abs">Get the latest news and updates from all things Lumetrix</p>
<div class="news-input abs">Your email address</div>
<a class="btn-solid news-submit abs">Subscribe</a>
<div class="footer-rule abs"></div>
<nav class="footer-col abs" style="left:170px"><h4>Product</h4><ul><li>Product</li><li>Case studies</li><li>Pricing</li></ul></nav>
<nav class="footer-col abs" style="left:400px"><h4>Company</h4><ul><li>About us</li><li>Contact us</li></ul></nav>
<nav class="footer-col abs" style="left:630px"><h4>Follow us</h4><ul><li>Linkora</li></ul></nav>
<nav class="footer-col abs" style="left:859px"><h4>Legal</h4><ul><li>Terms</li><li>Privacy policy</li><li>Cookie policy</li><li>EULA</li><li>DPA</li></ul></nav>
<p class="copyright abs">Copyright © 2022 All Rights Reserved</p>

</body>
</html>
```